Highlight Document Over Image for Slide

We are seeking a graphic designer to overlay a news article on an image that pertains to the article, aiming for a stylish yet professional appearance. Given the limited resources, we encourage you to use your imagination and go beyond what basic tools like PowerPoint can offer.

```html
<!DOCTYPE html>
<html lang="en">
<head>
<meta charset="UTF-8">
<title>Introduction or Possession of Contraband Items</title>
<link href="https://fonts.googleapis.com/css2?family=Archivo+Black&family=Oswald:wght@400;500&family=Roboto+Condensed:wght@400;500;700&display=swap" rel="stylesheet">
<style>
  :root {
    --stage: #2b2b2b;
    --paper: #f1efe9;
    --navy: #1f2a4c;
    --crimson: #8e1c34;
    --slash: #c0283f;
    --white: #ffffff;
    --slate: #6f716a;
    --land-tan: #a69674;
    --land-dry: #8d7f62;
    --roof-grey: #8a8c8a;
    --roof-light: #b9b8b1;
    --water: #71736b;
    --water-deep: #66685f;
    --fur-light: #c88d4f;
    --fur-mid: #a06a37;
    --fur-dark: #5b3a20;
  }
  * { box-sizing: border-box; margin: 0; padding: 0; }
  html, body { width: 1200px; height: 1200px; overflow: hidden; background: var(--stage); }
  .slide {
    position: absolute; left: 86px; top: 270px; width: 1046px; height: 612px;
    background: var(--slate); overflow: hidden;
  }
  .title-band {
    position: absolute; left: 0; top: 0; width: 1046px; height: 56px;
    background: var(--paper); border-bottom: 4px solid var(--crimson); z-index: 2;
  }
  .title {
    position: absolute; left: 20px; top: 11px;
    font-family: "Archivo Black", sans-serif; font-size: 31px; letter-spacing: 0.5px;
    color: var(--navy); white-space: nowrap;
  }
  .aerial-photo {
    position: absolute; left: 0; top: 56px; width: 1046px; height: 556px;
    background:
      radial-gradient(ellipse 150px 110px at 380px 200px, rgba(190,188,180,0.75), rgba(190,188,180,0) 100%),
      radial-gradient(ellipse 130px 90px at 170px 170px, rgba(150,148,140,0.7), rgba(150,148,140,0) 100%),
      radial-gradient(ellipse 170px 70px at 560px 150px, rgba(140,140,136,0.55), rgba(140,140,136,0) 100%),
      linear-gradient(170deg, var(--land-tan) 0%, var(--land-dry) 22%, var(--roof-grey) 42%, #7f7d72 52%, var(--water) 62%, var(--water-deep) 100%);
  }
  .dog-photo {
    position: absolute; left: 505px; top: 370px; width: 175px; height: 225px;
    background:
      radial-gradient(ellipse 28% 22% at 62% 20%, var(--fur-light), rgba(200,141,79,0) 100%),
      radial-gradient(ellipse 48% 40% at 45% 66%, var(--fur-mid) 0%, rgba(91,58,32,0.85) 60%, rgba(91,58,32,0) 100%);
  }
  .headline-box {
    position: absolute; left: 683px; top: 2px; width: 336px; height: 62px;
    background: var(--crimson); z-index: 3;
    font-family: "Oswald", sans-serif; font-weight: 400; font-size: 40px; line-height: 62px;
    color: var(--white); text-align: center; letter-spacing: 1px;
  }
  .panel {
    position: absolute; left: 683px; top: 64px; width: 336px; height: 527px;
    background: var(--navy); border-bottom: 4px solid var(--crimson); z-index: 2;
    color: var(--white); font-family: "Roboto Condensed", sans-serif;
  }
  .items-tab {
    position: absolute; left: 108px; top: 6px; width: 112px; height: 30px;
    background: var(--white); color: var(--navy);
    font-family: "Oswald", sans-serif; font-weight: 500; font-size: 22px; line-height: 30px;
    text-align: center; letter-spacing: 1.5px;
  }
  .items-tab::after {
    content: ""; position: absolute; left: 50%; bottom: -7px; margin-left: -7px;
    border-left: 7px solid transparent; border-right: 7px solid transparent; border-top: 7px solid var(--white);
  }
  .rule-text {
    position: absolute; left: 0; top: 54px; width: 336px; text-align: center;
    font-size: 16px; font-weight: 500; line-height: 19px; letter-spacing: 0.3px;
  }
  .rule-text u { text-underline-offset: 2px; }
  .icon-cell { position: absolute; }
  .icon-cell svg { display: block; }
  .icon-label {
    position: absolute; text-align: center;
    font-size: 12px; font-weight: 500; line-height: 13px; letter-spacing: 0.2px;
  }
  .authorized-note {
    position: absolute; left: 222px; top: 336px; width: 100px; text-align: center;
    font-size: 12px; font-weight: 500; line-height: 13px;
  }
  .authority-list {
    position: absolute; left: 32px; top: 424px; width: 290px; list-style: none;
    font-size: 13px; font-weight: 500; line-height: 16px; letter-spacing: 0.2px;
  }
  .authority-list li { position: relative; padding-left: 12px; }
  .authority-list li::before {
    content: ""; position: absolute; left: 0; top: 6px; width: 5px; height: 5px;
    border-radius: 50%; background: var(--slash);
  }
  .stroke { fill: none; stroke: var(--white); stroke-width: 2.6; stroke-linecap: round; stroke-linejoin: round; }
  .fill { fill: var(--white); }
  .bar { stroke: var(--slash); stroke-width: 3; stroke-linecap: round; }
</style>
</head>
<body>
<div class="slide">
  <div class="aerial-photo" role="img" aria-label="Aerial photograph of a waterfront correctional facility with buildings, yards, roads and the bay"></div>
  <div class="dog-photo" role="img" aria-label="Photograph of a seated police detection dog wearing a harness"></div>

  <div class="title-band"><h1 class="title">INTRODUCTION OR POSSESSION OF</h1></div>
  <div class="headline-box">[CONTRABAND]</div>

  <div class="panel">
    <div class="items-tab">ITEMS</div>
    <p class="rule-text">EMPLOYEES <u>SHALL NOT</u> INRODUCE OR<br>POSSESS UNAUTHORIZED ITEMS SUCH AS</p>

    <div class="icon-cell" style="left:21px;top:110px">
      <svg width="78" height="46" viewBox="0 0 78 46">
        <path class="stroke" d="M9 2H2V44H9M69 2H76V44H69"/>
        <circle class="stroke" cx="28" cy="28" r="9"/><circle class="stroke" cx="50" cy="28" r="9"/>
        <path class="stroke" d="M28 19V12H50V19"/>
        <line class="bar" x1="14" y1="42" x2="64" y2="5"/>
      </svg>
    </div>
    <div class="icon-label" style="left:11px;top:162px;width:98px">ESCAPE<br>PARAPHERNALIA</div>

    <div class="icon-cell" style="left:127px;top:110px">
      <svg width="82" height="46" viewBox="0 0 82 46">
        <path class="stroke" d="M9 2H2V44H9M73 2H80V44H73"/>
        <rect class="fill" x="20" y="28" width="42" height="9" rx="2"/>
        <path class="stroke" d="M30 28V16M52 28V16"/>
        <path class="stroke" d="M35 12Q41 7 47 12M32 8Q41 1 50 8"/>
        <line class="bar" x1="14" y1="42" x2="68" y2="5"/>
      </svg>
    </div>
    <div class="icon-label" style="left:117px;top:162px;width:102px">WIRELESS<br>COMMUNICATION<br>DEVICES</div>

    <div class="icon-cell" style="left:233px;top:110px">
      <svg width="82" height="46" viewBox="0 0 82 46">
        <path class="stroke" d="M9 2H2V44H9M73 2H80V44H73"/>
        <rect class="stroke" x="31" y="6" width="20" height="34" rx="3"/>
        <line class="stroke" x1="38" y1="35" x2="44" y2="35"/>
        <line class="bar" x1="14" y1="42" x2="68" y2="5"/>
      </svg>
    </div>
    <div class="icon-label" style="left:233px;top:162px;width:82px">CELLPHONES</div>

    <div class="icon-cell" style="left:18px;top:224px">
      <svg width="142" height="46" viewBox="0 0 142 46">
        <path class="stroke" d="M9 2H2V44H9M133 2H140V44H133"/>
        <rect class="fill" x="18" y="30" width="40" height="7" rx="1"/>
        <path class="stroke" d="M48 24Q44 18 50 12M56 24Q52 18 58 12"/>
        <rect class="fill" x="88" y="20" width="26" height="20" rx="3"/>
        <rect class="fill" x="95" y="10" width="12" height="8" rx="1"/>
        <line class="bar" x1="16" y1="42" x2="70" y2="6"/>
        <line class="bar" x1="80" y1="42" x2="126" y2="8"/>
      </svg>
    </div>
    <div class="icon-label" style="left:0;top:276px;width:170px">TOBACCO OR FACSIMILES OF<br>TOBACCO PRODUCTS E.G:<br>ELECTRONIC VAPOR CIGARETTES</div>

    <div class="icon-cell" style="left:162px;top:224px">
      <svg width="153" height="46" viewBox="0 0 153 46">
        <path class="stroke" d="M9 2H2V44H9M144 2H151V44H144"/>
        <path class="fill" d="M16 14H50V22H30L26 36H18L21 22H16Z"/>
        <path class="fill" d="M62 30L96 12L99 17L66 35Z"/>
        <path class="fill" d="M112 34L134 10L138 14L117 37Z"/>
        <line class="bar" x1="14" y1="42" x2="52" y2="6"/>
        <line class="bar" x1="64" y1="42" x2="98" y2="6"/>
        <line class="bar" x1="108" y1="42" x2="142" y2="6"/>
      </svg>
    </div>
    <div class="icon-label" style="left:182px;top:276px;width:120px">WEAPONS OR<br>FACSIMILES<br>OF WEAPONS</div>

    <div class="icon-cell" style="left:18px;top:330px">
      <svg width="76" height="46" viewBox="0 0 76 46">
        <path class="stroke" d="M9 2H2V44H9M67 2H74V44H67"/>
        <rect class="fill" x="29" y="20" width="18" height="22" rx="3"/>
        <path class="fill" d="M38 5Q44 12 38 17Q32 12 38 5Z"/>
        <line class="bar" x1="14" y1="42" x2="62" y2="5"/>
      </svg>
    </div>
    <div class="icon-label" style="left:18px;top:382px;width:76px">LIGHTER</div>

    <div class="icon-cell" style="left:125px;top:330px">
      <svg width="80" height="46" viewBox="0 0 80 46">
        <path class="stroke" d="M9 2H2V44H9M71 2H78V44H71"/>
        <path class="fill" d="M24 40V18Q28 8 32 18V40Z"/>
        <path class="fill" d="M36 40V18Q40 8 44 18V40Z"/>
        <path class="fill" d="M48 40V18Q52 8 56 18V40Z"/>
        <line class="bar" x1="14" y1="42" x2="66" y2="5"/>
      </svg>
    </div>
    <div class="icon-label" style="left:120px;top:382px;width:90px">AMMUNITION</div>

    <p class="authorized-note">OR ANY OTHER<br>ITEM NOT<br>SPECIFICALLY<br>AUTHORIZED BY:</p>

    <ul class="authority-list">
      <li>PD04.04.100 CUSTODY</li>
      <li>SECURITY &amp; SAFETY SYSTEMS (EXEMPT)</li>
      <li>OP 04.04.100 GATE SECURITY, OR</li>
      <li>FACILITY OPERATING PROCEDURE IN ANY<br>FACILITY OFFENDERS ARE HOUSED.</li>
    </ul>
  </div>
</div>
</body>
</html>
```